Landscaping flier 2024

Create a 1 page flier for landscaping services
1. Must be completed in Adobe Photoshop
2. Size 8.5" x 11" (portrait layout)
3. Include logo
4. Text to include:
2024 Gravesite Landscaping Packages
info@elmbrookmemorial.org
(201) 555-0143
elmbrookmemorial.org
5. Use chart text for the content. DO NOT COPY THE CHART DESIGN/FORMAT. Use the chart for the text you need only.
6. Use "Pricing cards as format for laying out the chart". Open to other ideas as well.
**Use the example of chart design (handwritten) to base your design off of.
7. Photos
-include before and after care photos

```html
<!DOCTYPE html>
<html lang="en">
<head>
<meta charset="utf-8">
<title>2024 Gravesite Landscaping Packages</title>
<link href="https://fonts.googleapis.com/css2?family=Oswald:wght@300;500;700&family=Montserrat:wght@400;500;600;700&family=Great+Vibes&display=swap" rel="stylesheet">
<style>
:root{
  --green:#1f9473;
  --green-dark:#167a5e;
  --green-soft:#7fc2ae;
  --teal-mist:#a7cfc8;
  --card:#d3e1de;
  --paper:#f1f1f0;
  --ink:#1d1d1d;
  --backdrop:#e6e6e6;
  --white:#ffffff;
}
*{margin:0;padding:0;box-sizing:border-box}
html,body{width:1200px;height:900px;overflow:hidden;background:var(--backdrop)}
.flier{position:absolute;left:298px;top:23px;width:604px;height:854px;background:var(--paper);overflow:hidden;font-family:"Montserrat",sans-serif;color:var(--ink)}
.abs{position:absolute}
.title{left:26px;top:36px;color:var(--white);font-family:"Oswald",sans-serif;line-height:1}
.title .year{font-weight:700;font-size:35px;letter-spacing:.5px;display:block;margin-bottom:4px}
.title .bold{font-weight:700;font-size:48px;display:block;margin-bottom:1px}
.title .mid{font-weight:500;font-size:48px;display:block;margin-bottom:1px}
.title .light{font-weight:300;font-size:48px;display:block}
.logo{left:449px;top:25px;width:96px;height:118px;background:var(--white);display:flex;flex-direction:column;align-items:center;justify-content:center;gap:8px}
.logo .mark{width:26px;height:26px;border-radius:50%;background:var(--green)}
.logo .name{font-family:"Montserrat",sans-serif;font-weight:600;font-size:11px;color:var(--green-dark);text-align:center;line-height:1.3}
.script{font-family:"Great Vibes",cursive;font-size:36px;color:#3a3a3a;top:365px}
.services{left:25px;top:428px;font-weight:700;font-size:24px;line-height:1.2;color:var(--green);letter-spacing:.3px}
.row-label{left:29px;font-weight:700;font-size:10.5px;line-height:1.25;text-transform:uppercase}
.col{top:421px;height:393px;width:133px;background:var(--card);border-radius:8px;overflow:hidden}
.col-head{height:66px;padding-top:6px;text-align:center;border-bottom:1px solid #b9cbc6}
.col-head h3{font-weight:500;font-size:14px;line-height:1.25;color:var(--green);text-transform:uppercase}
.col-head p{font-size:6px;font-weight:600;line-height:1.3;margin-top:4px}
.col.featured .col-head{background:var(--green);padding-top:13px}
.col.featured .col-head h3,.col.featured .col-head p{color:var(--white)}
.cell{position:absolute;left:0;width:100%;text-align:center;font-size:6px;font-weight:600;line-height:1.3}
.mark-x,.mark-tick{position:absolute;left:50%;width:10px;height:10px;margin-left:-5px}
.price{position:absolute;left:0;bottom:0;width:100%;height:69px;text-align:center;color:var(--green)}
.price .note{font-size:6px;margin-top:9px}
.price .amount{font-size:15px;font-weight:500;margin-top:4px}
.price .small{font-size:6px;color:var(--ink);margin-top:4px;line-height:1.3}
.col.featured .price{background:var(--green);color:var(--white)}
.col.featured .price .small{color:var(--white)}
.terms{display:flex;justify-content:space-around;padding:6px 4px 0}
.terms span{background:var(--green);color:var(--white);font-size:6.5px;padding:1px 5px;border-radius:5px}
.amounts{display:flex;justify-content:space-around;font-size:15px;font-weight:500;margin-top:3px}
.badge{left:471px;top:411px;background:var(--white);border:1.5px solid var(--green);border-radius:8px;color:var(--green);font-weight:600;font-size:11px;padding:1px 7px}
.valid{left:29px;top:780px;font-size:6px}
.footer{left:0;top:827px;width:604px;height:27px;background:var(--green);color:var(--white);font-weight:600;font-size:10.5px;display:flex;align-items:center;justify-content:center;gap:48px}
.footer .item{display:flex;align-items:center;gap:6px}
.footer svg{width:12px;height:12px}
</style>
</head>
<body>
<div class="flier">
  <!-- decorative shapes -->
  <svg class="abs" style="left:0;top:0" width="604" height="854" viewBox="0 0 604 854">
    <path d="M12 52 Q12 25 45 25 L200 25 Q262 25 262 110 Q262 230 150 258 Q60 275 22 225 Q12 210 12 180 Z" fill="var(--green)"/>
    <path d="M215 18 Q240 18 242 44 Q222 48 214 30 Z" fill="var(--teal-mist)"/>
    <path d="M255 78 Q248 20 300 0 Q306 48 255 78 Z" fill="var(--green)"/>
    <path d="M555 327 Q604 338 604 400 Q560 380 555 327 Z" fill="var(--green-soft)"/>
    <path d="M0 680 Q55 640 55 700 Q55 790 0 810 Z" fill="var(--teal-mist)"/>
    <defs>
      <linearGradient id="scene" x1="0" y1="0" x2="0" y2="1">
        <stop offset="0" stop-color="#a9c4df"/><stop offset=".35" stop-color="#b59a4f"/>
        <stop offset=".55" stop-color="#8a3a2a"/><stop offset=".75" stop-color="#5f8a3a"/><stop offset="1" stop-color="#5a5d5c"/>
      </linearGradient>
      <linearGradient id="grave" x1="0" y1="0" x2="0" y2="1">
        <stop offset="0" stop-color="#9aa49a"/><stop offset=".4" stop-color="#3f7a2e"/><stop offset="1" stop-color="#6fae3d"/>
      </linearGradient>
    </defs>
    <path role="img" aria-label="Cemetery grounds in autumn with a red maple, headstones and a paved path" d="M300 20 L520 20 Q538 20 538 40 L538 230 Q538 360 420 384 Q300 400 262 300 Q240 230 262 120 Q280 20 300 20 Z" fill="url(#scene)" stroke="var(--green)" stroke-width="3"/>
    <circle role="img" aria-label="Before photo: overgrown gravesite" cx="81" cy="310" r="65" fill="url(#grave)" stroke="var(--green)" stroke-width="3"/>
    <circle role="img" aria-label="After photo: neatly planted boxwood bed at gravesite" cx="222" cy="310" r="65" fill="url(#grave)" stroke="var(--green)" stroke-width="3"/>
  </svg>

  <h1 class="abs title"><span class="year">2024</span><span class="bold">Gravesite</span><span class="mid">Landscaping</span><span class="light">Packages</span></h1>

  <div class="abs logo"><span class="mark"></span><span class="name">Elmbrook<br>Memorial</span></div>

  <span class="abs script" style="left:36px">Before</span>
  <span class="abs script" style="left:185px">After</span>

  <h2 class="abs services">SERVICES<br>OFFERED</h2>

  <div class="abs row-label" style="top:505px">Weeding &amp; Trimmiing<br>on your gravesite</div>
  <div class="abs row-label" style="top:545px">Payment ensures<br>grave care forever</div>
  <div class="abs row-label" style="top:581px">Monument leveling</div>
  <div class="abs row-label" style="top:610px">Monument cleaning</div>
  <div class="abs row-label" style="top:645px">Full bed of boxwood<br>shrubs</div>
  <div class="abs row-label" style="top:685px">Replacement<br>of shrubs</div>
  <div class="abs row-label" style="top:719px">Trust certificate</div>

  <svg width="0" height="0" style="position:absolute">
    <symbol id="x" viewBox="0 0 10 10"><path d="M1.5 1.5 L8.5 8.5 M8.5 1.5 L1.5 8.5" stroke="#222" stroke-width="1.1"/></symbol>
    <symbol id="tick" viewBox="0 0 10 10"><path d="M1.5 5.5 L4 8 L8.5 2" stroke="#222" stroke-width="1.1" fill="none"/></symbol>
  </svg>

  <div class="abs col" style="left:174px">
    <div class="col-head"><h3>Seasonal<br>Care</h3><p>Seasonal landscaping<br>grave care.</p></div>
    <div class="cell" style="top:84px">Approximately every 7 weeks<br>during the growing season:<br>mid-April through mid-October</div>
    <svg class="mark-x" style="top:125px"><use href="#x"/></svg>
    <svg class="mark-x" style="top:160px"><use href="#x"/></svg>
    <svg class="mark-x" style="top:189px"><use href="#x"/></svg>
    <svg class="mark-x" style="top:224px"><use href="#x"/></svg>
    <svg class="mark-x" style="top:263px"><use href="#x"/></svg>
    <svg class="mark-x" style="top:298px"><use href="#x"/></svg>
    <div class="price">
      <div class="terms"><span>3 Years</span><span>2 Years</span><span>1 Year</span></div>
      <div class="amounts"><span>$396</span><span>$264</span><span>$132</span></div>
      <div class="small">Multi-year payment locks<br>in current rates</div>
    </div>
  </div>

  <div class="abs col" style="left:312px">
    <div class="col-head" style="padding-top:13px"><h3>Basic Care<br>Endowment</h3><p>Landscaping care forever<br>for graves with no plantings.</p></div>
    <div class="cell" style="top:87px">2 times per year: mid-May<br>&amp; mid September</div>
    <svg class="mark-tick" style="top:125px"><use href="#tick"/></svg>
    <svg class="mark-tick" style="top:160px"><use href="#tick"/></svg>
    <svg class="mark-x" style="top:189px"><use href="#x"/></svg>
    <svg class="mark-x" style="top:224px"><use href="#x"/></svg>
    <svg class="mark-x" style="top:263px"><use href="#x"/></svg>
    <svg class="mark-x" style="top:298px"><use href="#x"/></svg>
    <div class="price">
      <div class="note">12 Mounthly Payments of</div>
      <div class="amount">$287</div>
      <div class="small">Call for single payement discount</div>
    </div>
  </div>

  <div class="abs col featured" style="left:450px">
    <div class="col-head"><h3>Perpetual Care<br>Endowment</h3><p>Landscaping care forever<br>for graves with plantings.</p></div>
    <div class="cell" style="top:84px">Approximately every 7 weeks<br>during the growing season:<br>mid-April through mid-October</div>
    <svg class="mark-tick" style="top:125px"><use href="#tick"/></svg>
    <svg class="mark-tick" style="top:160px"><use href="#tick"/></svg>
    <svg class="mark-tick" style="top:189px"><use href="#tick"/></svg>
    <svg class="mark-tick" style="top:224px"><use href="#tick"/></svg>
    <svg class="mark-tick" style="top:263px"><use href="#tick"/></svg>
    <svg class="mark-tick" style="top:298px"><use href="#tick"/></svg>
    <div class="price">
      <div class="note">12 Mounthly Payments of</div>
      <div class="amount">$351</div>
      <div class="small">Call for single payement discount</div>
    </div>
  </div>

  <div class="abs badge">Most Popular</div>
  <div class="abs valid">Valid Through 10/31/2022</div>

  <div class="abs footer">
    <span class="item"><svg viewBox="0 0 12 12"><path d="M2.5 1 L4.5 1 L5.3 3.6 L4 4.6 Q5 7 7.4 8 L8.4 6.7 L11 7.5 L11 9.5 Q11 11 9.5 11 Q1 10.5 1 2.5 Q1 1 2.5 1 Z" fill="#fff"/></svg>(201) 555-0143</span>
    <span class="item"><svg viewBox="0 0 12 12" fill="none" stroke="#fff" stroke-width="1"><circle cx="6" cy="6" r="5"/><ellipse cx="6" cy="6" rx="2.2" ry="5"/><path d="M1 6 H11 M2 3.5 H10 M2 8.5 H10"/></svg>elmbrookmemorial.org</span>
    <span class="item"><svg viewBox="0 0 12 12" fill="none" stroke="#fff" stroke-width="1"><rect x="1" y="2.5" width="10" height="7"/><path d="M1 2.5 L6 7 L11 2.5"/></svg>info@elmbrookmemorial.org</span>
  </div>
</div>
</body>
</html>
```